Quiet Harbor Home Sales is a company designed to assist distressed homeowners short sell their property

Quiet Harbor Home Sales is a company designed to assist distressed homeowners liquidate their real properties for less than is owed on their mortgage. We help consumers through a stressful and difficult period of time by becoming their liaisons and advocates. We work with mortgage lenders to negotiate a reduced payoff amount that will satisfy all parties involved including the buyer, seller, and junior lien holders.

Target Market(s)

Distressed homeowner, Real estate Brokers & Agents

Industry/Entity Type

Real Estate

Coding

Coded - Design and coding required

Number of Pages Required

3 page

Font styles to use
Sans Serif

Requirements
Must have
• Small, simple, and elegant header. Must have a large photo under the header that fits within the screen, without having to scroll down to view the entire image. It should include a few simple words on the cover photo with a call to action, that does not cover the intended image or placed on the side. Under the large photo, we would like to have the ability to add additional content that can be a preview to other pages. This content would be viewed by scrolling down. We would like colors that work well with our logo. We are also requesting that the design be coded and fully developed in WordPress. Our current domain is purchased, quietharborhomesales.com and will be hosted by Hostmerry.
Nice to have
• Example website: https://www.plimvora.com/snaps/about/?page=home or http://www.quenzal.com/ or https://www.darvik.com/. We like to have the picture on the first page have some sort of action, such as zooming in to the picture.
Should not have
• Should not have too many variant colors. Should not feel too busy. No pop-ups.

```html
<!DOCTYPE html>
<html lang="en">
<head>
<meta charset="utf-8">
<title>Quiet Harbor Home Sales</title>
<link href="https://fonts.googleapis.com/css2?family=Lato:wght@300;400;700;900&display=swap" rel="stylesheet">
<style>
:root{
  --orange:#f0822f;
  --orange-dark:#e06f1a;
  --ink:#2f2f2f;
  --muted:#8a8a8a;
  --light:#f4f4f4;
  --dark:#3a3a3a;
  --darker:#4a4a4a;
  --black:#0d0d0d;
  --white:#ffffff;
}
*{box-sizing:border-box;margin:0;padding:0}
html,body{width:1200px;height:2656px;overflow:hidden}
body{font-family:"Lato",Arial,sans-serif;color:var(--ink);background:var(--white)}
.page{width:1200px;height:2656px;position:relative}

/* header */
.site-header{height:112px;display:flex;align-items:center;justify-content:space-between;padding:0 40px 0 30px;background:var(--white)}
.brand{display:flex;align-items:center;gap:10px;font-weight:900;font-size:24px;color:var(--ink)}
.brand-mark{width:14px;height:14px;background:var(--orange)}
.main-nav{display:flex;gap:40px;font-size:14px}
.main-nav a{color:var(--ink);text-decoration:none}
.main-nav a.active{color:var(--orange)}

/* hero */
.hero{height:528px;position:relative;background:linear-gradient(180deg,#aebdd0 0%,#8797ad 40%,#5e6470 70%,#7d7d78 100%)}
.hero-copy{position:absolute;right:80px;top:90px;width:300px;text-align:right;color:var(--white)}
.hero-copy h1{font-weight:400;font-size:40px;line-height:1.1;margin-bottom:12px}
.hero-copy p{font-size:14px;line-height:1.5;margin-bottom:22px}
.btn{display:inline-block;background:var(--orange);color:var(--white);font-weight:700;font-size:14px;padding:14px 24px;text-decoration:none;letter-spacing:.5px}

/* section titles */
.section-title{text-align:center}
.section-title h2{font-weight:900;font-size:26px;letter-spacing:.5px}
.section-title p{font-size:18px;color:var(--muted);margin-top:6px}
.divider{width:220px;height:14px;margin:22px auto 0;display:block}

/* services */
.services{height:540px;padding-top:70px}
.service-grid{display:flex;justify-content:center;gap:0;margin-top:40px}
.service{width:250px;text-align:center;padding:0 20px}
.service svg{width:56px;height:56px}
.service h3{font-size:16px;font-weight:900;margin:20px 0 12px}
.service p{font-size:13px;color:var(--muted);line-height:1.5}

/* about */
.about{height:260px;background:var(--light);display:flex;align-items:center;padding:0 170px}
.about-photo{width:170px;height:170px;border-radius:50%;background:radial-gradient(circle at 50% 40%,#dce6ef,#a8bfd4);flex:none;border:6px solid var(--white)}
.about-body{margin-left:70px}
.about-body .kicker{font-size:20px;color:var(--muted)}
.about-body h2{font-size:22px;font-weight:900;margin:2px 0 6px}
.about-body .rule{width:60px;height:3px;background:var(--orange);margin-bottom:16px}
.about-body p{font-size:13px;color:var(--muted);line-height:1.7;max-width:620px}

/* blog */
.blog{height:480px;padding-top:60px}
.posts{display:flex;justify-content:center;gap:80px;margin-top:40px}
.post{display:flex;width:420px;gap:20px}
.post-image{width:200px;height:180px;flex:none;position:relative}
.post-image .date{position:absolute;top:10px;right:0;background:var(--orange);color:var(--white);font-size:11px;padding:4px 10px}
.post-image .date.dark{background:var(--dark)}
.post h3{font-size:17px;font-weight:900;line-height:1.3}
.post .meta{font-size:11px;color:var(--muted);margin:10px 0}
.post p{font-size:12px;color:var(--muted);line-height:1.6}

/* contact band */
.contact-band{height:480px;background:var(--dark);display:flex;justify-content:center;gap:90px;padding-top:40px}
.column{width:450px}
.column-head{text-align:center;color:var(--white);margin-bottom:26px}
.column-head span{display:block;font-size:18px;color:#bbb}
.column-head strong{font-size:20px;font-weight:900;letter-spacing:.5px}
.testimonial{background:var(--orange);height:300px;text-align:center;color:var(--white);padding:34px 50px}
.testimonial h4{font-size:17px;font-weight:700}
.testimonial .role{font-size:11px;opacity:.85;margin-bottom:24px}
.avatar{width:56px;height:56px;border-radius:50%;background:rgba(255,255,255,.35);margin:18px auto 0;border:3px solid var(--white)}
.testimonial p{font-size:13px;line-height:1.6;margin-top:10px}
.contact-form{background:var(--darker);height:300px;padding:30px 30px}
.field-row{display:flex;gap:16px;margin-bottom:16px}
.field{flex:1;height:34px;background:#5c5c5c;color:#bbb;font-size:11px;padding:10px 12px}
.field.message{height:90px}
.form-foot{text-align:center}
.btn-small{display:inline-block;background:var(--orange);color:var(--white);font-size:11px;font-weight:700;padding:9px 16px}

/* footer */
.site-footer{height:256px;background:var(--black);text-align:center;color:#ccc;padding-top:90px}
.foot-nav{display:flex;justify-content:center;gap:48px;font-size:12px}
.foot-nav a{color:#ccc;text-decoration:none}
.foot-nav a.active{color:var(--white)}
.copyright{font-size:12px;margin-top:26px}
.social{display:flex;justify-content:center;gap:12px;margin-top:12px}
.social span{width:9px;height:9px;border-radius:50%;background:#ccc}
</style>
</head>
<body>
<div class="page">

<header class="site-header">
  <div class="brand"><span class="brand-mark"></span>Quiet Harbor Home Sales</div>
  <nav class="main-nav">
    <a class="active" href="#">Home</a><a href="#">About Us</a><a href="#">Services</a><a href="#">Properties</a><a href="#">Videos</a><a href="#">Blog</a><a href="#">Contact Us</a>
  </nav>
</header>

<section class="hero" role="img" aria-label="Photo of a large two-storey suburban house with lit windows at dusk">
  <div class="hero-copy">
    <h1>Quiet Harbor Home Sales</h1>
    <p>We help distressed homeowners liquidate their real properties for less than is owed on their mortgage</p>
    <a class="btn" href="#">GET STARTED NOW</a>
  </div>
</section>

<section class="services">
  <div class="section-title">
    <h2>OUR SERVICES</h2>
    <p>Integer vitae libero ac risus egestas placerat</p>
    <svg class="divider" viewBox="0 0 220 14"><line x1="0" y1="7" x2="95" y2="7" stroke="#f0822f" stroke-width="2"/><polyline points="95,7 110,1 125,7" fill="none" stroke="#f0822f" stroke-width="2"/><line x1="125" y1="7" x2="220" y2="7" stroke="#f0822f" stroke-width="2"/></svg>
  </div>
  <div class="service-grid">
    <div class="service">
      <svg viewBox="0 0 56 56" fill="none" stroke="#f0822f" stroke-width="2"><circle cx="22" cy="20" r="8"/><path d="M8 44c0-9 6-14 14-14s14 5 14 14"/><circle cx="38" cy="24" r="6"/><path d="M36 34c7 0 12 4 12 10"/></svg>
      <h3>LOREM IPSUM</h3>
      <p>Vitae libero ac risus egestas placerat, lorem nunc dapibus elit sed congue.</p>
    </div>
    <div class="service">
      <svg viewBox="0 0 56 56" fill="none" stroke="#f0822f" stroke-width="2"><circle cx="28" cy="28" r="18"/><path d="M28 18v10l8 5"/><path d="M28 6v4M28 46v4M6 28h4M46 28h4"/></svg>
      <h3>DOLOR SIT AMIT</h3>
      <p>Praesent dapibus neque id cursus faucibus tortor neque egestas augue nibh.</p>
    </div>
    <div class="service">
      <svg viewBox="0 0 56 56" fill="none" stroke="#f0822f" stroke-width="2"><rect x="10" y="12" width="36" height="34" rx="2"/><path d="M10 22h36M18 8v8M38 8v8"/><path d="M17 30h5M25 30h5M33 30h5M17 38h5M25 38h5"/></svg>
      <h3>CONTANEY POPILAR</h3>
      <p>Donec eu libero sit amet quam egestas semper aenean ultricies mi vitae.</p>
    </div>
    <div class="service">
      <svg viewBox="0 0 56 56" fill="none" stroke="#f0822f" stroke-width="2"><rect x="12" y="10" width="32" height="38" rx="2"/><path d="M20 20h16M20 28h16M20 36h10"/><circle cx="40" cy="42" r="6" fill="#fff"/></svg>
      <h3>POPULAR SIT</h3>
      <p>Sed adipiscing ornare risus morbi est est blandit sit amet sagittis vel.</p>
    </div>
  </div>
</section>

<section class="about">
  <div class="about-photo" role="img" aria-label="Portrait photo of a smiling business team"></div>
  <div class="about-body">
    <div class="kicker">Lorem ipsum dolor sit</div>
    <h2>ABOUT US</h2>
    <div class="rule"></div>
    <p>We help consumers through a stressful and difficult period of time by becoming their liaisons and advocates. We work with mortgage lenders to negotiate a reduced payoff amount that will satisfy all parties involved, including the buyer, seller and junior lien holders, so every homeowner can move forward with confidence and a clear plan for the future.</p>
  </div>
</section>

<section class="blog">
  <div class="section-title">
    <h2>LATEST BLOG</h2>
    <p>Integer vitae libero ac risus egestas placerat</p>
    <svg class="divider" viewBox="0 0 220 14"><line x1="0" y1="7" x2="95" y2="7" stroke="#f0822f" stroke-width="2"/><polyline points="95,7 110,1 125,7" fill="none" stroke="#f0822f" stroke-width="2"/><line x1="125" y1="7" x2="220" y2="7" stroke="#f0822f" stroke-width="2"/></svg>
  </div>
  <div class="posts">
    <article class="post">
      <div class="post-image" role="img" aria-label="Photo of a row of brick townhouses" style="background:linear-gradient(180deg,#c9d6e2,#8b7a68)"><span class="date">12 Mar</span></div>
      <div>
        <h3>Lorem ipsum dolor sit amit contanty</h3>
        <div class="meta">2 days ago &nbsp;|&nbsp; 3 comments</div>
        <p>Lorem ipsum is simply dummy text of the printing and typesetting industry, used as a placeholder across many layouts and pages.</p>
      </div>
    </article>
    <article class="post">
      <div class="post-image" role="img" aria-label="Photo of a model house beside a stack of coins" style="background:linear-gradient(180deg,#f1e6d8,#c98a52)"><span class="date dark">08 Mar</span></div>
      <div>
        <h3>Contanty sit amit lome sit dol</h3>
        <div class="meta">5 days ago &nbsp;|&nbsp; 1 comment</div>
        <p>Lorem ipsum is simply dummy text of the printing and typesetting industry, used as a placeholder across many layouts and pages.</p>
      </div>
    </article>
  </div>
</section>

<section class="contact-band">
  <div class="column">
    <div class="column-head"><span>Our Clients</span><strong>TESTIMONIALS</strong></div>
    <div class="testimonial">
      <h4>Johny Doe</h4>
      <div class="role">Local homeowner</div>
      <div class="avatar" role="img" aria-label="Client portrait"></div>
      <p>"Integer vitae libero ac risus egestas placerat. They guided us through every step and made a difficult time far easier for our family."</p>
    </div>
  </div>
  <div class="column">
    <div class="column-head"><span>Contact Us</span><strong>FOR MORE INFORMATION</strong></div>
    <form class="contact-form">
      <div class="field-row"><div class="field">First name</div><div class="field">Last name</div></div>
      <div class="field-row"><div class="field">Email</div><div class="field">Phone</div></div>
      <div class="field-row"><div class="field message">Message</div></div>
      <div class="form-foot"><span class="btn-small">SUBMIT</span></div>
    </form>
  </div>
</section>

<footer class="site-footer">
  <nav class="foot-nav">
    <a class="active" href="#">Home</a><a href="#">About Us</a><a href="#">Services</a><a href="#">Properties</a><a href="#">Videos</a><a href="#">Blog</a><a href="#">Contact Us</a>
  </nav>
  <div class="copyright">Copyright © website name.</div>
  <div class="social"><span></span><span></span><span></span><span></span></div>
</footer>

</div>
</body>
</html>
```